Refer a Friend A5 Flyer for Healthcare Staff

We need an A5 flyer that we can hand out to existing and new staff members promoting our Refer a friend Scheme. We need the leaflet to encourage staff to talk to their family and friends about joining our Healthcare Agency, which provides staff to local care related establishments. Using our logo and brand colours blue and green, as per our website, the final design will need to clearly convey the benefits and attractions of referring additional staff to the team. In addition is the promotion of our SocialHub page, requesting staff to like the page and to like and share various posts.

Target Market(s)

Healthcare and potential Healthcare Staff

Industry/Entity Type

Healthcare

Colors
33b8a4
3277b5

Requirements
Must have
• Company Logo, Brand colours,
• text; "Refer a Friend and receive a £50 Bonus after just 1 completed shift"
• text; "3 easy steps to refer a friend, 1 Fill out your name on the back of your Business Card 2 Hand the card to your friend or any person you wish to refer, 3 ask your friend to present the card to us when they attend their interview"
• text; "Like and share any of our Open Days on SocialHub for a chance to win a prize, you can find us easily by searching @CarewellPlacementGroup"
• text; "Like our Page to stay up to date with our events and offers"
Nice to have
• care worker / elderly care / support worker pictures
• Content / pics from website www.carewellplacementgroup.co.uk

```html
<!DOCTYPE html>
<html lang="en">
<head>
<meta charset="utf-8">
<title>Carewell Placement – Refer a Friend Flyer</title>
<link href="https://fonts.googleapis.com/css2?family=Poppins:ital,wght@0,300;0,400;0,500;0,600;0,700;1,400&display=swap" rel="stylesheet">
<style>
  :root {
    --brand-blue: #1156a6;
    --brand-blue-deep: #0f4f9e;
    --brand-green: #17a98e;
    --tag-green: #1fa98a;
    --ink-grey: #7a7f85;
    --page-bg: #e9e6e1;
    --paper: #ffffff;
  }
  * { margin: 0; padding: 0; box-sizing: border-box; }
  html, body { width: 1099px; height: 1200px; overflow: hidden; }
  body {
    background: var(--page-bg);
    font-family: "Poppins", sans-serif;
    position: relative;
  }
  .flyer {
    position: absolute;
    left: 135px; top: 12px;
    width: 828px; height: 1176px;
    background: var(--paper);
    box-shadow: 0 4px 14px rgba(0,0,0,0.18);
    overflow: hidden;
  }
  .hero {
    position: absolute; left: 0; top: 0;
    width: 828px; height: 488px;
  }
  .hero-photo {
    position: absolute; inset: 0;
    background:
      linear-gradient(90deg, rgba(250,252,248,0.97) 0%, rgba(240,246,236,0.9) 35%, rgba(220,232,210,0.3) 55%, rgba(0,0,0,0) 65%),
      linear-gradient(180deg, #7fa46a 0%, #5f8b4d 35%, #b9a98c 75%, #9c9a80 100%);
  }
  .brand {
    position: absolute; left: 70px; top: 125px;
    display: flex; align-items: center; gap: 14px;
  }
  .brand-dot {
    width: 26px; height: 26px; border-radius: 50%;
    background: var(--brand-green);
  }
  .brand-name {
    font-weight: 400; font-size: 50px; line-height: 52px;
    color: var(--brand-blue);
    letter-spacing: -0.5px;
  }
  .brand-tagline {
    position: absolute; left: 297px; top: 234px;
    font-weight: 300; font-size: 16px; line-height: 18px; color: var(--ink-grey);
  }
  .values {
    position: absolute; left: 0; top: 284px; width: 512px;
    list-style: none; text-align: center;
  }
  .values li { margin-bottom: 5px; line-height: 0; }
  .values span {
    display: inline-block;
    background: var(--tag-green); color: #fff;
    font-size: 27px; font-weight: 400; line-height: 33px;
    padding: 0 4px;
  }
  .offer {
    position: absolute; left: 0; top: 488px;
    width: 828px; height: 267px;
    background: var(--brand-blue);
    color: #fff; text-align: center;
    display: flex; align-items: center; justify-content: center;
  }
  .offer h1 {
    font-weight: 500; font-size: 56px; line-height: 63px;
    letter-spacing: -0.3px;
  }
  .offer strong { font-weight: 700; }
  .steps {
    position: absolute; left: 0; top: 788px; width: 828px;
    text-align: center; color: var(--brand-blue-deep);
  }
  .steps h2 { font-weight: 600; font-size: 38px; line-height: 48px; }
  .steps ol { list-style: none; font-size: 17px; line-height: 23px; font-weight: 400; }
  .social {
    position: absolute; left: 30px; top: 945px;
    width: 763px; height: 194px;
    border-radius: 12px; overflow: hidden;
    color: #fff; text-align: center;
  }
  .social-invite {
    background: var(--brand-green);
    height: 138px;
    display: flex; align-items: center; justify-content: center;
  }
  .social-invite-text {
    display: block;
    font-size: 28px; line-height: 34px; font-weight: 400;
  }
  .social-invite strong { font-weight: 700; }
  .social-follow {
    background: var(--brand-blue);
    height: 56px;
    display: flex; align-items: center; justify-content: center;
    font-style: italic; font-size: 23px;
  }
</style>
</head>
<body>
  <main class="flyer">
    <section class="hero">
      <div class="hero-photo" role="img" aria-label="Photo of a smiling care worker in scrubs standing behind an elderly woman in a wheelchair in a sunny garden"></div>
      <div class="brand">
        <span class="brand-dot"></span>
        <div class="brand-name">Carewell<br>Placement</div>
      </div>
      <div class="brand-tagline">Keeping it Simple</div>
      <ul class="values">
        <li><span>SIMPLICITY</span></li>
        <li><span>SUPERIOR SOLUTIONS</span></li>
        <li><span>OFFICIALLY RECOGNIZED</span></li>
      </ul>
    </section>

    <section class="offer">
      <h1>Refer a Friend and<br>receive a <strong>£50</strong> Bonus after<br>just 1 completed shift</h1>
    </section>

    <section class="steps">
      <h2>3 easy steps to refer a friend</h2>
      <ol>
        <li>1. Fill out your name on the back of your Business Card</li>
        <li>2. Hand the card to your friend or any person you wish to refer</li>
        <li>3. ask your friend to present the card to us when they attend their interview</li>
      </ol>
    </section>

    <section class="social">
      <div class="social-invite">
        <p class="social-invite-text">Like and share any of our Open Days on <strong>SocialHub</strong><br>for a chance to win a prize, you can find us easily<br>by searching <strong>@CarewellPlacementGroup</strong></p>
      </div>
      <p class="social-follow">Like our Page to stay up to date with our events nd offers</p>
    </section>
  </main>
</body>
</html>
```